This is for a book cover design (front and back) and I need it to match my branding guidelines which I have attached below. I have also attached other books to show you what I'm looking for.

This book is about "A new way to make money online" which I believe is the best way to get to 7 figures FAST. So For the book I have a book example to give you all an example of what I am looking for but it still needs to be about digital online money and digital marketing.

The Book Title: The Golden Ladder Blueprint Codex
The Book Subtitle: Discover How To Sell Your Front End High Ticket Offers With No Sales Team, No VLS, No Phone Calls and Without Having A Huge Social Media Presence!

for the book could we go in the direction of having my face in the background and having it be like im the mastermind behind this revolutionary new way to make money. I included an image below to give you what the mind map could look like but you see how you have take the latest version we are almost there but not quite yet.
So in the middle of the mind map it would be a dollar sign $. The other pieces of the puzzle (or you could test one version out as puzzle pieces with the words on it below: So let's have two different versions - one with the mind map and one being puzzle pieces with the Center puzzle piece being $.
VIP Day
Challenges
Advertising
Identifying The BIG Problem
Webinars
Organic Reach
Trust Building
Value
Influencer Marketing
Gamification
Objection Handling
Artificial Intelligence
Applications
Financing
Email Marketing
Backends
Marketing Psychology
Sales
High Ticket Offers
Empathy Maps
List Building
Upsells
Customer Avatars
Podcasts
Webinars
Content Distribution
Customer Service
Merchant Processors
Systems
Sales
Still keeping the same look etc but testing out puzzle pieces with my face being the puzzle. Just thinking of something different and unique for my first book

• Puzzle Pieces & Mind Maps
• Utilize My Color Schemes

```html
<!DOCTYPE html>
<html lang="en">
<head>
<meta charset="utf-8">
<title>The Golden Ladder Blueprint Codex – Book Cover</title>
<link rel="stylesheet" href="https://fonts.googleapis.com/css2?family=Arimo:wght@400;700&display=swap">
<style>
  :root {
    --ink: #02030f;
    --brand-blue: #0ca3dc;
    --paper: #ffffff;
    --photo-glow: #1a2f8a;
    --photo-mid: #0a1240;
  }
  * { margin: 0; padding: 0; box-sizing: border-box; }
  html, body { width: 1200px; height: 904px; overflow: hidden; background: var(--ink); }
  body { font-family: "Arimo", Arial, sans-serif; color: var(--paper); }
  h1, h2, h3 { font-weight: 400; }

  .cover { position: relative; width: 1200px; height: 904px; background: var(--ink); }

  .back, .spine, .front { position: absolute; top: 0; height: 904px; }
  .back { left: 0; width: 565px; }
  .spine { left: 565px; width: 71px; background: var(--brand-blue); }
  .front { left: 636px; width: 564px; overflow: hidden; }

  .abs { position: absolute; }
  .center { text-align: center; white-space: nowrap; }

  /* ---------- Back cover ---------- */
  .back .kicker { top: 22px; left: 0; width: 565px; display: flex; align-items: center; justify-content: center; gap: 12px; font-size: 23px; letter-spacing: 2px; }
  .rule { display: block; height: 2px; background: var(--paper); }
  .back .kicker .rule { width: 75px; }
  .back .title-main { top: 60px; left: 0; width: 565px; font-size: 54px; letter-spacing: 9px; line-height: 1; padding-left: 9px; }
  .back .band { top: 122px; left: 0; width: 565px; height: 21px; background: var(--brand-blue); }
  .back .band-text { top: 122px; left: 0; width: 565px; font-size: 19px; line-height: 21px; letter-spacing: 5.2px; }
  .back .title-end { top: 158px; left: 0; width: 565px; font-size: 36px; letter-spacing: 8px; line-height: 1; padding-left: 8px; }

  .blurb { left: 30px; width: 505px; font-size: 10.6px; line-height: 12.7px; letter-spacing: 1.15px; text-transform: uppercase; text-align: center; }
  .blurb-1 { top: 255px; }
  .blurb-2 { top: 402px; }
  .blurb-3 { top: 536px; }

  .about-heading { top: 650px; left: 0; width: 565px; font-size: 34px; letter-spacing: 3.4px; line-height: 1; }
  .author-portrait-slot { top: 703px; left: 70px; width: 134px; height: 134px; background: var(--paper); }
  .author-bio { top: 705px; left: 218px; width: 304px; font-size: 10.6px; line-height: 12.8px; letter-spacing: 1.2px; text-transform: uppercase; text-align: center; }

  /* ---------- Spine ---------- */
  .spine-title { position: absolute; left: 0; top: 25px; width: 71px; height: 806px; display: flex; align-items: center; justify-content: center; }
  .spine-title span { writing-mode: vertical-rl; transform: rotate(180deg); font-weight: 700; font-size: 31px; color: var(--ink); white-space: nowrap; letter-spacing: 0.3px; }

  /* ---------- Front cover ---------- */
  .author-photo { top: 380px; left: 0; width: 564px; height: 467px;
    background: radial-gradient(ellipse 42% 55% at 52% 60%, var(--photo-glow) 0%, var(--photo-mid) 45%, var(--ink) 85%); }
  .front .kicker { top: 38px; left: 76px; width: 400px; display: flex; align-items: center; justify-content: center; gap: 20px; font-size: 44px; letter-spacing: 2px; line-height: 1; }
  .front .kicker .rule { width: 150px; height: 4px; }
  .front .title-main { top: 112px; left: 0; width: 564px; font-size: 96px; letter-spacing: 12px; line-height: 1; padding-left: 12px; }
  .front .band { top: 235px; left: 0; width: 564px; height: 44px; background: var(--brand-blue); }
  .front .band-text { top: 235px; left: 0; width: 564px; font-size: 34px; line-height: 44px; letter-spacing: 7px; padding-left: 7px; }
  .front .title-end { top: 305px; left: 0; width: 564px; font-size: 72px; letter-spacing: 24px; line-height: 1; padding-left: 24px; }
  .subtitle { top: 416px; left: 0; width: 564px; font-size: 15.8px; line-height: 19.4px; text-transform: uppercase; text-align: center; }

  .strategy-map { top: 490px; left: 0; width: 564px; height: 350px; }
  .map-link { stroke: var(--brand-blue); stroke-width: 1.2; opacity: 0.75; }
  .map-node rect { fill: var(--ink); fill-opacity: 0.78; stroke: var(--brand-blue); stroke-width: 1.2; }
  .map-node text { fill: var(--paper); font-family: "Arimo", Arial, sans-serif; font-size: 9.5px; text-anchor: middle; }
  .map-hub circle { fill: var(--brand-blue); }
  .map-hub text { fill: var(--paper); font-family: "Arimo", Arial, sans-serif; font-weight: 700; font-size: 40px; text-anchor: middle; }

  .author-band { top: 847px; left: 0; width: 564px; height: 57px; background: var(--brand-blue); }
  .author-name { top: 847px; left: 0; width: 564px; font-size: 40px; line-height: 57px; letter-spacing: 9px; padding-left: 9px; }
</style>
</head>
<body>
<main class="cover">

  <section class="back">
    <div class="abs kicker"><span class="rule"></span><span>THE</span><span class="rule"></span></div>
    <h2 class="abs center title-main">GOLDEN</h2>
    <div class="abs band"></div>
    <div class="abs center band-text">LADDER BLUEPRINT</div>
    <div class="abs center title-end">CODEX</div>

    <p class="abs blurb blurb-1">Lorem ipsum dolor sit amet, consectetur adipiscing elit, sed do eiusmod tempor incididunt ut labore et dolore magna aliqua. Quis ipsum suspendisse ultrices gravida. Risus commodo viverra maecenas accumsan lacus vel facilisis.Lorem ipsum dolor sit amet, consectetur adipiscing elit, sed do eiusmod tempor incididunt ut labore et dolore magna aliqua. Quis ipsum suspendisse ultrices gravida. Risus commodo viverra maecenas accumsan lacus vel facilisis.</p>
    <p class="abs blurb blurb-2">Lorem ipsum dolor sit amet, consectetur adipiscing elit, sed do eiusmod tempor incididunt ut labore et dolore magna aliqua. Quis ipsum suspendisse ultrices gravida. Risus commodo viverra maecenas accumsan lacus vel facilisis.Lorem ipsum dolor sit amet, consectetur adipiscing elit, sed do eiusmod tempor incididunt ut labore et dolore magna aliqua. Quis ipsum suspendisse ultrices gravida. Risus commodo viverra maecenas accumsan lacus vel facilisis.</p>
    <p class="abs blurb blurb-3">Lorem ipsum dolor sit amet, consectetur adipiscing elit, sed do eiusmod tempor incididunt ut labore et dolore magna aliqua. Quis ipsum suspendisse ultrices gravida. Risus commodo viverra maecenas accumsan lacus vel facilisis.Lorem ipsum dolor sit amet, consectetur adipiscing elit, sed do eiusmod tempor incididunt ut labore et dolore magna aliqua. Quis ipsum suspendisse ultrices gravida. Risus commodo viverra maecenas accumsan lacus vel facilisis.</p>

    <h3 class="abs center about-heading">ABOUT THE AUTHOR</h3>
    <div class="abs author-portrait-slot"></div>
    <p class="abs author-bio">Lorem ipsum dolor sit amet, consectetur adipiscing elit, sed do eiusmod tempor incididunt ut labore et dolore magna aliqua. Quis ipsum suspendisse ultrices gravida. Risus commodo viverra maecenas accumsan lacus vel facilisis.Lorem ipsum dolor sit amet, consectetur adipiscing elit, sed do eiusmod tempor incididunt ut labore et dolore magna aliqua. Quis ipsum</p>
  </section>

  <section class="spine">
    <div class="spine-title"><span>THE GOLDEN LADDER BLUEPRINT CODEX.</span></div>
  </section>

  <section class="front">
    <div class="abs author-photo" role="img" aria-label="Portrait of the author in a hooded top, lit in deep blue"></div>
    <div class="abs kicker"><span class="rule"></span><span>THE</span><span class="rule"></span></div>
    <h1 class="abs center title-main">GOLDEN</h1>
    <div class="abs band"></div>
    <div class="abs center band-text">LADDER BLUEPRINT</div>
    <div class="abs center title-end">CODEX</div>
    <p class="abs subtitle">Discover how to sell your front end high ticket offers<br>with no sales team, no VLS, no phone calls<br>and without having a huge social media presence!</p>

    <svg class="abs strategy-map" viewBox="0 0 564 350" aria-label="Mind map of online marketing strategies around a central dollar sign">
      <g class="map-links">
        <line class="map-link" x1="282" y1="175" x2="482" y2="175"/>
        <line class="map-link" x1="282" y1="175" x2="455" y2="107"/>
        <line class="map-link" x1="282" y1="175" x2="382" y2="58"/>
        <line class="map-link" x1="282" y1="175" x2="282" y2="40"/>
        <line class="map-link" x1="282" y1="175" x2="182" y2="58"/>
        <line class="map-link" x1="282" y1="175" x2="109" y2="107"/>
        <line class="map-link" x1="282" y1="175" x2="82" y2="175"/>
        <line class="map-link" x1="282" y1="175" x2="109" y2="242"/>
        <line class="map-link" x1="282" y1="175" x2="182" y2="292"/>
        <line class="map-link" x1="282" y1="175" x2="282" y2="310"/>
        <line class="map-link" x1="282" y1="175" x2="382" y2="292"/>
        <line class="map-link" x1="282" y1="175" x2="455" y2="242"/>
      </g>
      <g class="map-node"><rect x="420" y="165" width="124" height="20" rx="10"/><text x="482" y="178.5">Advertising</text></g>
      <g class="map-node"><rect x="393" y="97" width="124" height="20" rx="10"/><text x="455" y="110.5">Webinars</text></g>
      <g class="map-node"><rect x="320" y="48" width="124" height="20" rx="10"/><text x="382" y="61.5">Trust Building</text></g>
      <g class="map-node"><rect x="220" y="30" width="124" height="20" rx="10"/><text x="282" y="43.5">High Ticket Offers</text></g>
      <g class="map-node"><rect x="120" y="48" width="124" height="20" rx="10"/><text x="182" y="61.5">Email Marketing</text></g>
      <g class="map-node"><rect x="47" y="97" width="124" height="20" rx="10"/><text x="109" y="110.5">Sales</text></g>
      <g class="map-node"><rect x="20" y="165" width="124" height="20" rx="10"/><text x="82" y="178.5">Systems</text></g>
      <g class="map-node"><rect x="47" y="232" width="124" height="20" rx="10"/><text x="109" y="245.5">Upsells</text></g>
      <g class="map-node"><rect x="120" y="282" width="124" height="20" rx="10"/><text x="182" y="295.5">List Building</text></g>
      <g class="map-node"><rect x="220" y="300" width="124" height="20" rx="10"/><text x="282" y="313.5">Customer Avatars</text></g>
      <g class="map-node"><rect x="320" y="282" width="124" height="20" rx="10"/><text x="382" y="295.5">Artificial Intelligence</text></g>
      <g class="map-node"><rect x="393" y="232" width="124" height="20" rx="10"/><text x="455" y="245.5">Objection Handling</text></g>
      <g class="map-hub"><circle cx="282" cy="175" r="34"/><text x="282" y="189">$</text></g>
    </svg>

    <div class="abs author-band"></div>
    <div class="abs center author-name">MARCUS HALE</div>
  </section>

</main>
</body>
</html>
```